Letter and Envelope Design For Larchmont Realty

Please design a letter and an envelope incorporating our logo (See Attached). We are also launched a business card contest. Since we want them to match, please feel free to submit a design for both the business card and also the letter design and envelope.

Requirements
Must have
• The envelope, the letter and the business cards must match somehow connecting the designs. We want them to have something that holds them together besides the logo.

```html
<!DOCTYPE html>
<html lang="en">
<head>
<meta charset="utf-8">
<title>Larchmont Realty – Letterhead and Envelopes</title>
<link href="https://fonts.googleapis.com/css2?family=Questrial&family=Roboto:wght@400&display=swap" rel="stylesheet">
<style>
  :root{
    --brand-blue:#021b8c;
    --ink:#3b3b3b;
    --body-ink:#555;
    --paper:#f6f6f6;
    --backdrop:#dcdcdc;
    --watermark:#e6e7ee;
    --rule-grey:#6b6b6b;
    --white:#fff;
  }
  *{box-sizing:border-box;margin:0;padding:0}
  html,body{width:1200px;height:877px;overflow:hidden;background:var(--backdrop)}
  .canvas{position:relative;width:1200px;height:877px}
  .sheet{position:absolute;background:var(--paper);overflow:hidden}

  /* Letterhead */
  .letterhead{left:69px;top:64px;width:528px;height:742px}
  .watermark{position:absolute;border-radius:50%;border:7px solid var(--watermark)}
  .letterhead .watermark{left:120px;top:233px;width:312px;height:312px}
  .brand{position:absolute;text-align:center;color:var(--brand-blue);font-family:"Questrial",sans-serif}
  .brand-dot{display:block;margin:0 auto;border:2.5px solid var(--brand-blue);border-radius:50%}
  .brand-name{display:block;letter-spacing:2px;line-height:1.15;text-transform:uppercase}
  .letterhead .brand{left:164px;top:44px;width:200px}
  .letterhead .brand-dot{width:46px;height:46px;margin-bottom:9px}
  .letterhead .brand-name{font-size:13.5px}
  .letter-body{position:absolute;left:46px;top:206px;width:440px;font-family:"Questrial",sans-serif;color:var(--body-ink)}
  .salutation{font-size:13.6px;color:var(--ink);margin-bottom:26px}
  .letter-body p{font-size:7.6px;line-height:11.4px;margin-bottom:11.4px;text-align:justify}
  .letter-body p.closing{margin-top:22px;text-align:left}
  .signature{position:absolute;left:42px;top:520px;width:94px;height:36px;background:linear-gradient(90deg,#c9d0ef,#dfe3f5);border-radius:4px}
  .footer-band{position:absolute;left:0;bottom:0;width:528px;height:34px}
  .footer-text{position:absolute;left:0;bottom:4px;width:100%;text-align:center;color:var(--white);font-family:"Roboto",sans-serif;font-size:8px;line-height:10.5px}

  /* Envelope back */
  .envelope-back{left:614px;top:269px;width:531px;height:240px}
  .flap{position:absolute;left:0;top:0}

  /* Envelope front */
  .envelope-front{left:614px;top:563px;width:533px;height:242px}
  .envelope-front .watermark{left:317px;top:23px;width:192px;height:192px;border-width:5px}
  .envelope-front .brand{left:20px;top:25px;width:120px}
  .envelope-front .brand-dot{width:40px;height:40px;margin-bottom:7px}
  .envelope-front .brand-name{font-size:11px;letter-spacing:1.6px}
  .return-address{margin-top:5px;font-family:"Roboto",sans-serif;font-size:8px;line-height:10px;color:var(--ink);letter-spacing:0}
  .envelope-front .footer-band{height:30px;width:533px}
</style>
</head>
<body>
<div class="canvas">

  <section class="sheet letterhead">
    <div class="watermark"></div>
    <div class="brand">
      <span class="brand-dot"></span>
      <span class="brand-name">Larchmont<br>Realty</span>
    </div>
    <div class="letter-body">
      <div class="salutation">Dear Mr. Harlow,</div>
      <p>Lorem ipsum dolor sit amet, consectetur adipiscing elit. Donec orci purus, luctus vitae dignissim eu, iaculis sed purus. Vivamus faucibus, ipsum nec aliquet viverra, leo mauris condimentum ligula, sit amet sagittis enim ligula quis arcu. Nam egestas tortor id nisi porttitor mattis. In tortor ante, ultricies in suscipit a, tempus non massa. Vivamus et auctor mi. Fusce vel massa nulla. Phasellus nec eros mauris, et scelerisque orci.</p>
      <p>Donec malesuada orci vitae nulla accumsan porta a id massa. Quisque accumsan iaculis magna sit amet fringilla. Maecenas consequat, magna eget tincidunt semper, odio nibh rutrum mi, id feugiat ante nisi eu risus. Vestibulum nunc orci, rhoncus a placerat in, ultricies in mi. Cras mattis varius eros, vel fringilla nisi suscipit eget. Quisque scelerisque sagittis nulla at porttitor.</p>
      <p>Sed id augue vitae urna euismod commodo aliquet a quam. Pellentesque arcu velit, cursus et malesuada ut, consequat et diam. Nullam erat sem, rhoncus id ullamcorper vitae, rhoncus et arcu. In ultricies ultricies nulla, ut rutrum nisi iaculis at. Donec eu magna a metus ornare faucibus. Fusce aliquet faucibus ultricies. Morbi semper, est id tincidunt gravida, sem arcu adipiscing lacus, ac bibendum nulla leo eu purus. Quisque nec diam sed risus consectetur a cumsan quis quis nibh. Vestibulum id purus lorem.</p>
      <p>It is a long established fact that a reader will be distracted by the readable content of a page when looking at its layout. The point of using Lorem Ipsum is that it has a more-or-less normal distribution of letters, as opposed to using 'Content here, content here', making it look like readable English. Many desktop publishing packages</p>
      <p class="closing">Sincerely,</p>
    </div>
    <div class="signature" role="img" aria-label="Handwritten signature of Daniel Harlow"></div>
    <svg class="footer-band" viewBox="0 0 528 34" preserveAspectRatio="none">
      <path d="M0 12 Q264 -8 528 12" fill="none" stroke="var(--rule-grey)" stroke-width="1.4"/>
      <path d="M0 16 Q264 -4 528 16 L528 34 L0 34Z" fill="var(--brand-blue)"/>
    </svg>
    <div class="footer-text">
      4120 Willow Crest Road, Juneau, Alaska 34581<br>
      P. 555 014 2290 F. 555 014 2291 E. hello@larchmontrealty.test W. www.larchmontrealty.test
    </div>
  </section>

  <section class="sheet envelope-back">
    <svg class="flap" width="531" height="76" viewBox="0 0 531 76">
      <path d="M0 0 H531 L524 40 Q520 74 486 74 H45 Q12 74 7 40 Z" fill="var(--brand-blue)"/>
      <circle cx="266" cy="39" r="16" fill="none" stroke="var(--white)" stroke-width="2"/>
    </svg>
  </section>

  <section class="sheet envelope-front">
    <div class="watermark"></div>
    <div class="brand">
      <span class="brand-dot"></span>
      <span class="brand-name">Larchmont<br>Realty</span>
      <div class="return-address">4120 Willow Crest Road<br>Juneau, Alaska 34581</div>
    </div>
    <svg class="footer-band" viewBox="0 0 533 30" preserveAspectRatio="none">
      <path d="M0 12 Q266 -8 533 12" fill="none" stroke="var(--rule-grey)" stroke-width="1.4"/>
      <path d="M0 16 Q266 -4 533 16 L533 30 L0 30Z" fill="var(--brand-blue)"/>
    </svg>
  </section>

</div>
</body>
</html>
```